Simple Postcard Design

We want to have Quillo do a mailing for our new real estate company. We have roughed a sketch of what we would like. A picture of the property on one side and the copy on the reverse side.Attached are the files.

POSTCARD Size-8.52" x 5.47" **********

Target Market(s)

Residents of our town

Industry/Entity Type

Real Estate

Font styles to use
Serif

Colors
00a990

Requirements
Must have
• Look of elegance
Nice to have
• NO NO Border on picture,,,,,banner on 45 in top left corner
• "New Listing"

```html
<!DOCTYPE html>
<html lang="en">
<head>
<meta charset="utf-8">
<title>Vista Realtors – Postcard</title>
<link href="https://fonts.googleapis.com/css2?family=Tinos:ital,wght@0,400;1,400&display=swap" rel="stylesheet">
<style>
  :root {
    --bg: #e9e6e1;
    --card: #ffffff;
    --ink: #1a1a1a;
    --rule: #b9b9b9;
    --water-deep: #14202a;
    --water: #22323e;
    --sand: #d8c7a6;
    --green: #3f5a34;
  }
  * { margin: 0; padding: 0; box-sizing: border-box; }
  html, body { width: 1015px; height: 1200px; overflow: hidden; }
  body {
    background: var(--bg);
    position: relative;
    font-family: "Tinos", "Times New Roman", serif;
    color: var(--ink);
  }
  .card {
    position: absolute;
    background: var(--card);
    box-shadow: 0 2px 6px rgba(0,0,0,0.18);
  }
  .card--front { left: 64px; top: 47px; width: 808px; height: 525px; }
  .card--back { left: 140px; top: 617px; width: 807px; height: 523px; }

  .property-photo {
    position: absolute;
    left: 29px; top: 22px; width: 744px; height: 481px;
    border-radius: 12px;
    background:
      radial-gradient(ellipse 40% 30% at 62% 62%, #cdbb98 0%, rgba(205,187,152,0) 100%),
      radial-gradient(ellipse 35% 28% at 78% 85%, #6a7a4a 0%, rgba(106,122,74,0) 100%),
      linear-gradient(160deg, #8a8a84 0%, #5d6560 22%, var(--water) 40%, var(--sand) 62%, var(--green) 85%, var(--water-deep) 100%);
  }

  .brand-name {
    position: absolute;
    left: 37px; top: 52px;
    font-size: 30px;
    font-weight: 400;
    line-height: 36px;
    color: var(--ink);
  }
  .office {
    position: absolute;
    left: 37px; top: 133px;
    font-size: 15px;
    line-height: 16.4px;
    font-style: normal;
  }
  .listing {
    position: absolute;
    left: 37px; top: 216px; width: 332px;
    font-size: 16.4px;
    line-height: 19.4px;
    text-align: justify;
    hyphens: auto;
  }
  .contact {
    position: absolute;
    left: 37px; top: 393px;
    font-size: 15px;
    line-height: 17px;
  }
  .disclaimer {
    position: absolute;
    left: 37px; top: 436px; width: 352px;
    font-size: 12.2px;
    line-height: 17px;
    font-style: italic;
    text-align: justify;
  }
  .stamp-box {
    position: absolute;
    left: 680px; top: 39px; width: 92px; height: 64px;
    border: 1px solid var(--rule);
  }
  .address-lines {
    position: absolute;
    left: 537px; top: 180px;
  }
</style>
</head>
<body>
  <section class="card card--front">
    <div class="property-photo" role="img" aria-label="Aerial photograph of the waterfront estate with pool, dock and neighbouring canal homes"></div>
  </section>

  <section class="card card--back">
    <div class="brand-name">Vista Realtors</div>

    <address class="office">
      48 Harbor Lane<br>
      Bayhaven, NJ 08700<br>
      555 014-2000<br>
      www.VistaRealtors.com
    </address>

    <p class="listing">This unique 1.68 acre estate in South Bayhaven has 644" of water front. The 22 room house features a 2 story master suite, 6 guest bedrooms, large living room, great room with 2 fireplaces, in law Suite, 15 car garage, in ground pool, brick patio, numerous porches and a 200" Dock.<br>Priced at $4,995,000.</p>

    <p class="contact">For more information contact Quillo<br>555 016-3188</p>

    <p class="disclaimer">If your property is listed with a real estate broker, please disregard. It is not our intention to solicit the offerings of other real estate brokers.</p>

    <div class="stamp-box"></div>

    <svg class="address-lines" width="246" height="120" viewBox="0 0 246 120" aria-hidden="true">
      <g stroke="#b9b9b9" stroke-width="1.2">
        <line x1="0" y1="1" x2="246" y2="1"/>
        <line x1="0" y1="30" x2="246" y2="30"/>
        <line x1="0" y1="59" x2="246" y2="59"/>
        <line x1="0" y1="88" x2="246" y2="88"/>
        <line x1="0" y1="117" x2="246" y2="117"/>
      </g>
    </svg>
  </section>
</body>
</html>
```